Fontenot Bayou Grillhouse (Owners Card)

Need a classy, but modern business card. I have included a promotional card for the steakhouse. I need one for myself (the owner) that is more professional.

Target Market(s)

General Public

Industry/Entity Type

Food service

Contact Information for Business Card

Name, business address, phone number, email, logo

Font styles to use
Serif
Sans Serif
Decorative
Script

Requirements
Must have
• My name (Darvel Pruitt), business address (327 Oakmere Street), phone number (510) 493-2615, email (Dpruittkr4@mailvane.example. On the back of the card: Psalms 27 1 The LORD is my light and my salvation— whom shall I fear? The LORD is the stronghold of my life— of whom shall I be afraid? 2 When the wicked advance against me to devour me, it is my enemies and my foes who will stumble and fall. 3 Though an army besiege me, my heart will not fear; though war break out against me, even then I will be confident.
Nice to have
• Something that’s bold, but modern and professional.

```html
<!DOCTYPE html>
<html lang="en">
<head>
<meta charset="utf-8">
<title>Fontenot Bayou Grillhouse – Owner Business Card</title>
<link href="https://fonts.googleapis.com/css2?family=Patua+One&family=Cabin:wght@400&display=swap" rel="stylesheet">
<style>
  :root {
    --page-bg: #ffffff;
    --card-dark: #221f20;
    --card-glow: #5b5d62;
    --text-light: #ffffff;
    --label-grey: #7a7a7a;
    --brand-orange: #f08a24;
    --icon-green: #7cb342;
    --icon-amber: #f5a623;
    --icon-orange: #f07f1e;
    --icon-red: #e8531f;
    --shadow: rgba(0,0,0,0.85);
  }
  * { margin: 0; padding: 0; box-sizing: border-box; }
  html, body { width: 1200px; height: 1000px; overflow: hidden; background: var(--page-bg); }
  body { position: relative; font-family: "Patua One", serif; }

  .card {
    position: absolute; left: 281px; width: 638px; height: 364px;
    background: var(--card-dark); overflow: hidden; color: var(--text-light);
  }
  .card--front { top: 89px;
    background: radial-gradient(ellipse 300px 260px at 470px 190px, var(--card-glow), var(--card-dark) 100%); }
  .card--back { top: 548px;
    background: radial-gradient(ellipse 330px 260px at 200px 130px, var(--card-glow), var(--card-dark) 100%); }

  .crest-decoration {
    position: absolute; border-radius: 50%;
    background: radial-gradient(ellipse at center, rgba(30,28,30,0.45), rgba(30,28,30,0) 70%);
  }
  .card--front .crest-decoration { left: 240px; top: 70px; width: 370px; height: 230px; }
  .card--back .crest-decoration { left: 40px; top: 20px; width: 380px; height: 230px; }

  .brand-name {
    position: absolute; color: var(--brand-orange); text-align: center;
    font-family: "Patua One", serif; line-height: 1.15;
  }
  .card--front .brand-name { left: 30px; top: 150px; width: 290px; font-size: 30px; }
  .card--back .brand-name { left: 440px; top: 60px; width: 180px; font-size: 20px; }

  .holder { position: absolute; left: 330px; top: 52px; width: 290px; text-align: center; text-shadow: 2px 2px 3px var(--shadow); }
  .holder__name { font-size: 36px; letter-spacing: 1.8px; line-height: 1.2; }
  .holder__title { font-size: 18px; letter-spacing: 1.5px; margin-top: 2px; }

  .contact { position: absolute; left: 339px; top: 175px; list-style: none; }
  .contact__item { display: flex; align-items: flex-start; font-size: 17px; letter-spacing: 1.2px; line-height: 23px; margin-bottom: 12px; text-shadow: 2px 2px 3px var(--shadow); }
  .contact__item--email { font-size: 16px; letter-spacing: 0.7px; }
  .contact__icon { width: 18px; height: 18px; margin: 2px 12px 0 0; flex: none; }

  .verse { position: absolute; left: 41px; top: 116px; text-shadow: 2px 2px 3px var(--shadow); }
  .verse__title { font-size: 20px; letter-spacing: 1.3px; margin-bottom: 6px; }
  .verse__line { font-size: 13.5px; letter-spacing: 1.65px; line-height: 26.4px; white-space: nowrap; }
  .verse__line--indent { padding-left: 17px; }

  .side-label { position: absolute; left: 0; width: 1200px; text-align: center; font-family: "Cabin", sans-serif; font-size: 16px; color: var(--label-grey); }
</style>
</head>
<body>

<section class="card card--front">
  <div class="crest-decoration" role="img" aria-label="Faint large crest ornament in the background"></div>
  <div class="brand-name">Fontenot Bayou<br>Grillhouse</div>

  <div class="holder">
    <div class="holder__name">Darvel Pruitt</div>
    <div class="holder__title">Owner</div>
  </div>

  <ul class="contact">
    <li class="contact__item">
      <svg class="contact__icon" viewBox="0 0 18 18"><path d="M9 1a6 6 0 0 0-6 6c0 4.5 6 10 6 10s6-5.5 6-10a6 6 0 0 0-6-6z" fill="var(--icon-green)"/><circle cx="9" cy="7" r="2.3" fill="var(--card-dark)"/></svg>
      <span>327 Oakmere Street<br>Marlow Springs, CA 94718</span>
    </li>
    <li class="contact__item">
      <svg class="contact__icon" viewBox="0 0 18 18"><path d="M4 2l3 0 1.5 4-2 1.3a9 9 0 0 0 4.2 4.2L12 9.5l4 1.5v3a2 2 0 0 1-2 2A13 13 0 0 1 2 4a2 2 0 0 1 2-2z" fill="var(--icon-amber)"/></svg>
      <span>(510) 493-2615</span>
    </li>
    <li class="contact__item contact__item--email">
      <svg class="contact__icon" viewBox="0 0 18 18"><rect x="1" y="4" width="16" height="11" fill="var(--icon-orange)"/><path d="M1.5 4.5L9 10l7.5-5.5" stroke="var(--card-dark)" stroke-width="1.4" fill="none"/></svg>
      <span>Dpruittkr4@mailvane.example</span>
    </li>
    <li class="contact__item">
      <svg class="contact__icon" viewBox="0 0 18 18"><circle cx="9" cy="9" r="8" fill="var(--icon-red)"/><g stroke="var(--card-dark)" stroke-width="1" fill="none"><ellipse cx="9" cy="9" rx="3.5" ry="8"/><path d="M1 9h16M2.5 5h13M2.5 13h13M9 1v16"/></g></svg>
      <span>Fontbayou.example</span>
    </li>
  </ul>
</section>
<div class="side-label" style="top:483px">Front Side</div>

<section class="card card--back">
  <div class="crest-decoration" role="img" aria-label="Faint large crest ornament in the background"></div>
  <div class="brand-name">Fontenot Bayou<br>Grillhouse</div>

  <div class="verse">
    <div class="verse__title">Psalms 27</div>
    <p class="verse__line">1 The LORD is my light and my salvation</p>
    <p class="verse__line">— whom shall I fear? The LORD is the stronghold of my life</p>
    <p class="verse__line">— of whom shall I be afraid?</p>
    <p class="verse__line">2 When the wicked advance against me to devour me, it is my enemies</p>
    <p class="verse__line verse__line--indent">and my foes who will stumble and fall.</p>
    <p class="verse__line">3 Though an army besiege me, my heart will not fear; though war break</p>
    <p class="verse__line verse__line--indent">out against me, even then I will be confident.</p>
  </div>
</section>
<div class="side-label" style="top:942px">Back Side</div>

</body>
</html>
```